Specialist Technical Theatre service for schools

The task is to design a brochure (A5, 4 pages) for mailing to secondary/high school heads and drama departments to sell them our services as Technical Theatre and Drama professionals who can help them to offer elements of a curriculum that they do not currently offer as well as raise the technical standards of their school productions.
Please find a document attached which outlines the content for the brochure. Please read the document first so that you understand our aims. The text highlighted in yellow takes priority - the text highlighted in blue could be used if there is space.
Photos which may be used available on https://www.snapvault.example/photos/ben_torvik/ (please do not use watermarked morrow pictures).
Logo is attached (two variants) - one of which should appear somewhere on the design. Website address is www.bentorvik.co.uk and email is info@bentorvik.co.uk
Target Market(s)
Theatre and Drama teachers in Secondary/High schools
Headteachers of Secondary/High Schools
Industry/Entity Type
Education
Look and feel

```html
<!DOCTYPE html>
<html lang="en">
<head>
<meta charset="utf-8">
<title>Ben Torvik – Stage and Production Management brochure, inside spread</title>
<link href="https://fonts.googleapis.com/css2?family=Crimson+Text:wght@400;600&display=swap" rel="stylesheet">
<style>
  :root{
    --canvas:#e9e9e9;
    --page:#050505;
    --gold:#f6c431;
    --bronze:#6e5a2c;
    --text-gold:#e9b93a;
    --text-light:#d9d9d9;
    --white:#ffffff;
  }
  *{margin:0;padding:0;box-sizing:border-box}
  html,body{width:1200px;height:1000px;overflow:hidden;background:var(--canvas)}
  body{position:relative;font-family:"Crimson Text",Georgia,serif}
  .spread{position:absolute;left:60px;top:183px;width:1085px;height:757px;background:var(--page);box-shadow:0 18px 30px rgba(0,0,0,.35)}
  .page{position:absolute;top:0;height:757px;overflow:hidden;background:var(--page)}
  .page--left{left:0;width:543px}
  .page--right{left:543px;width:542px}
  .page-shapes{position:absolute;inset:0;width:100%;height:100%}
  .photo{position:absolute}
  .photo--concert{left:0;top:18px;width:543px;height:140px;background:linear-gradient(180deg,#2a1f1c 0%,#5a2d3a 35%,#7a3a50 55%,#1a1212 100%)}
  .photo--concert::after{content:"";position:absolute;inset:0;background:linear-gradient(180deg,rgba(0,0,0,0) 55%,#050505 100%)}
  .photo--rigging{left:0;top:417px;width:255px;height:172px;background:linear-gradient(180deg,#9a9a9a,#4e4e4e)}
  .photo--seating{left:258px;top:417px;width:285px;height:172px;background:linear-gradient(180deg,#1b2d55,#2d4c8a)}
  .photo--hall{left:0;top:592px;width:255px;height:165px;background:linear-gradient(180deg,#3a2a6a,#1c2350)}
  .photo--retracted{left:258px;top:592px;width:285px;height:165px;background:linear-gradient(180deg,#2a2a2e,#5a6a85)}
  .photo--procession{left:12px;top:237px;width:530px;height:330px;background:radial-gradient(ellipse at 55% 35%,#6a6a66 0%,#2e2c2a 50%,#050505 100%)}
  .brand{position:absolute;left:55px;top:42px;width:140px;text-align:center;color:var(--white)}
  .brand__row{display:flex;align-items:center;justify-content:center;gap:6px}
  .brand__dot{width:12px;height:12px;border-radius:50%;background:var(--bronze)}
  .brand__name{font-size:17px;font-weight:400;line-height:1}
  .brand__tag{margin-top:8px;font-size:8px;letter-spacing:.5px;line-height:1.25;text-transform:uppercase}
  .body-copy{position:absolute;color:var(--text-gold);font-size:11.6px;line-height:13.8px;text-align:justify}
  .body-copy--intro{left:52px;top:153px;width:440px;text-indent:14px}
  .body-copy--marks{left:52px;top:253px;width:440px;text-indent:14px}
  .headline{position:absolute;left:55px;top:356px;width:440px;color:var(--white);font-size:17px;line-height:20px}
  .right-copy{position:absolute;left:30px;width:488px;color:var(--text-light);font-size:11px;line-height:12.8px;text-align:justify}
  .right-copy--top{top:37px}
  .right-copy p{margin-bottom:12px}
  .credentials{list-style:none;color:var(--text-gold);margin-top:-12px}
  .credentials li{position:relative;padding-left:12px}
  .credentials li::before{content:"";position:absolute;left:2px;top:5px;width:3px;height:3px;background:var(--text-gold)}
  .right-copy--bottom{top:571px}
  .right-copy--bottom p{margin-bottom:0}
  .right-copy--bottom .note{margin-top:10px}
</style>
</head>
<body>
<main class="spread">
  <section class="page page--left">
    <div class="photo photo--concert" role="img" aria-label="Live concert stage with coloured lighting and audience"></div>
    <svg class="page-shapes" viewBox="0 0 543 757" preserveAspectRatio="none" aria-hidden="true">
      <polygon points="0,0 200,0 0,40" fill="var(--gold)"/>
      <polygon points="200,0 543,0 543,12" fill="var(--bronze)"/>
      <polygon points="0,757 543,757 543,730 150,745" fill="var(--bronze)"/>
      <polygon points="0,725 0,757 130,757" fill="var(--gold)"/>
    </svg>
    <div class="brand">
      <div class="brand__row"><span class="brand__dot"></span><span class="brand__name">Ben Torvik</span></div>
      <div class="brand__tag">Stage and<br>production management</div>
    </div>
    <p class="body-copy body-copy--intro">As live theatre and performance becomes an increasingly important part of the global economy, there is currently a huge demand for Technical and Production Management professionals. We are able to support you with training your students in the specialist skills and knowledge of managing creative processes from initial concept through rehearsal to realised performance.</p>
    <p class="body-copy body-copy--marks">With 60% of marks being allocated to the practical elements of ‘creating original drama’ and ‘making theatre’ you would like to offer your students the opportunity to pursue the technical design elements of the course but don’t have the technical support? NQB A-level Drama and Theatre and Pearline GCSE Drama (from September 2016)</p>
    <h2 class="headline">You would like someone with the specialist knowledge to ensure that your students meet the assessment criteria?</h2>
    <div class="photo photo--rigging" role="img" aria-label="Sports hall with staging truss and flight cases being rigged"></div>
    <div class="photo photo--seating" role="img" aria-label="Empty blue tiered auditorium seating"></div>
    <div class="photo photo--hall" role="img" aria-label="Hall lit in purple with seating and lighting rig"></div>
    <div class="photo photo--retracted" role="img" aria-label="Retractable blue seating in a studio theatre"></div>
    <svg class="page-shapes" viewBox="0 0 543 757" preserveAspectRatio="none" aria-hidden="true">
      <polygon points="0,757 543,757 543,735 160,740 0,728" fill="var(--bronze)"/>
      <polygon points="0,730 0,757 120,757" fill="var(--gold)"/>
    </svg>
  </section>

  <section class="page page--right">
    <svg class="page-shapes" viewBox="0 0 542 757" preserveAspectRatio="none" aria-hidden="true">
      <polygon points="0,0 542,0 542,28 300,12" fill="var(--bronze)"/>
      <polygon points="300,0 542,0 542,22" fill="var(--gold)"/>
      <polygon points="542,757 200,757 360,725 542,712" fill="var(--gold)"/>
      <polygon points="360,725 200,757 330,757 380,733" fill="var(--bronze)"/>
    </svg>
    <div class="right-copy right-copy--top">
      <p>Your school and Drama Department owns a wide range of technical theatre equipment that isn’t used to its full potential?</p>
      <p>You have a school wide musical, play or dance performance approaching and would like to get a student crew motivated, trained and involved in the technical aspects of the performance?</p>
      <p>If your answer to any of the above is ‘Yes’ then we can help.</p>
      <ul class="credentials">
        <li>DBS checked staff (subscribed to the DBS update service so you can run an instant check on our arrival)</li>
        <li>Qualified in Technical Theatre (through a Stagecraft UK accredited establishment)</li>
        <li>ISWP certified (we adopt the latest safe working practice)</li>
        <li>First Aid Qualified (just in case!)</li>
        <li>Experience of working with Children and Young People in Education (includes previous experience of teaching production skills to GCSE and A-Level students and Youth theatre)</li>
        <li>Currently working in the Theatre and Events Industry (we bring current industry knowledge to you and your students)</li>
      </ul>
    </div>
    <div class="photo photo--procession" role="img" aria-label="Students in dark cloaks carrying a coffin through stage smoke"></div>
    <div class="right-copy right-copy--bottom">
      <p>Whether its technical assistance with a one-off school production, practical examination performance support, weekly Technical Theatre Design curriculum delivery or workshops introducing Year 9 to the opportunities offered through Drama GCSE we can help you to find a solution.</p>
      <p>Budget tight? From £250 to £380 per day* depending on the requirement we are experts at working to academic budgets. We will always deliver the aims of the course using your school and department equipment; however, in order to ensure that your students are familiar with the latest technology we do include any specialist equipment (i.e LED lighting, Framewise editing suite, smoke machines etc.) within the cost.</p>
      <p class="note">*Discount available if booking consecutive days, mileage charges apply.</p>
    </div>
  </section>
</main>
</body>
</html>
```